PathVerdantia Community/ Talent Gallery

PathVerdantia is developing a collaborative career course, with coaching and community exchange. Goal is to offer a platform where talented candidates can show their expertise and find projects, partners, and develop their online portfolios!

Here is a good example of the type of thing we hope to create with focus on sustainability focused talent to task matching
http://www.halbrook-example.com/global-themes/employment-and-growth/connecting-talent-with-opportunity-in-the-digital-age

We hope to have a "grid style" gallery where it is easy to search by talent types and focus areas within the scope of "Sustainability" issues...Food/Water/Energy, Public Health, Technology, Sustainable Cities, Infrastructure, Education, Policy, Emerging Economies, Ecosystems, Social Innovation, inclusive Security, Equity Issues. For each topic/ header we hope to have candidates post their completed portfolios to exhibit resumes, biography, a case study... they may actually prepare these on other sites, but can link in OR alternately that they can easily create here, similar to "tellyou.biz" ....

Hope to include a blog space titled "Steering Through Seams", where people can mix it up across these topic issues as they are interdependent and often require partners across discipline areas! If possible another area where jobs related to these issues may be posted as project or job opportunities by potential employers.

If there is a way to create a feed from various job sites that already exist...like Jobrix...or http://www.greenventurehub-example.com/ that would be super great. Again...sort of a portal connection to bridge the gap ....instead of candidates having to search all the time, we are hoping they can advertise their talent and employers may search here for these well presented portfolios!

Target Market(s)

Educators, Students, Career Transitioners, Employers, Professional Associations, Talent Recruiters with focus on Sustainability related Talent to Task matching!

Industry/Entity Type

Sustainability

Number of Pages Required

4 page

Font styles to use
Sans Serif

Colors
3176b5
32b8a4
add136

Requirements
Must have
• Not sure about the coded/ uncoded option here....
• Must have - grid style area where Sustainability Professionals with varied focus areas can exhibit their talent portfolios
• appear as a Talent Gallery that starts with photos & obvious organization...other tabs to be in a menu.
• ability to search both talent and task opportunity areas to help coaches or community members make matches....some topic focused category or tag words to help make them searchable...???
• consistent professional styling to existing website and new artflock postcard shared in brief/ images area
• Interactive blog space where articles, issues may be posted, discussed
• Bulletin board or feed for project opportunities to be posted where candidates may locate them and/or employers may express specific "call" for talent..These may be Short term Internships, Projects, Consulting Team Opportunity, or Jobs/ part time to full time....
Nice to have
• A calendar area where we can post networking opportunities, issues presentations where potential partners can meet the next generation leaders, attend a forum or webinar presentation.
Should not have
• Too much text on front page...Should be clean design,

```html
<!DOCTYPE html>
<html lang="en">
<head>
<meta charset="utf-8">
<title>PathVerdantia — Talent Gallery</title>
<link rel="stylesheet" href="https://fonts.googleapis.com/css2?family=Roboto:wght@300;400;500;700&display=swap">
<style>
:root{
  --teal:#32b8a4;
  --teal-dark:#2aa592;
  --blue:#3176b5;
  --blue-bright:#1b84c9;
  --green:#8cc63f;
  --orange:#ff9800;
  --sky:#17b1e8;
  --ink:#333;
  --muted:#777;
  --line:#e3e3e3;
  --panel:#f6f7f7;
}
*{box-sizing:border-box;margin:0;padding:0}
html,body{width:1200px;height:2655px;overflow:hidden}
body{font-family:'Roboto',sans-serif;color:var(--ink);background:#fff;position:relative}
.abs{position:absolute}

/* header */
.topbar{left:0;top:0;width:1200px;height:50px;background:var(--teal);color:#fff}
.brand{left:88px;top:11px;display:flex;align-items:center;gap:9px;font-size:16px;font-weight:500}
.brand-dot{width:28px;height:28px;border-radius:50%;background:#fff;opacity:.9}
.nav{left:545px;top:0;display:flex;height:50px;font-size:12px}
.nav a{color:#fff;text-decoration:none;padding:19px 12px 0}
.nav a.active{background:rgba(255,255,255,.2);border-top:3px solid #fff;padding-top:16px}
.account{left:975px;top:18px;display:flex;gap:26px;font-size:12px}
.account span{display:flex;align-items:center;gap:6px}

/* hero */
.hero{left:0;top:50px;width:1200px;height:558px;background:linear-gradient(120deg,#8a8a72 0%,#c9c5a6 30%,#4f5a66 60%,#2c3440 100%)}
.hero-arrow{width:34px;height:34px;background:rgba(0,0,0,.55);top:318px}
.hero-arrow.right{background:var(--green)}
.hero-card{left:720px;top:397px;width:392px;height:211px;background:var(--blue-bright);color:#fff;text-align:center}
.hero-card .site{margin-top:40px;font-size:12px;display:flex;justify-content:center;align-items:center;gap:12px}
.hero-card .site::before,.hero-card .site::after{content:"";width:68px;height:1px;background:#fff}
.hero-card h2{font-weight:300;font-size:38px;margin-top:14px}
.hero-card p{font-weight:300;font-size:26px;margin-top:2px}
.dots{display:flex;justify-content:center;gap:4px;margin-top:28px}
.dots i{width:9px;height:9px;border:1px solid #fff;border-radius:50%}
.dots i.on{background:#fff}

/* welcome */
.welcome{left:0;top:648px;width:1200px;text-align:center}
.welcome h3{font-weight:300;font-size:22px}
.welcome h1{font-weight:300;font-size:34px;margin-top:2px}
.welcome p{font-size:12px;color:#555;line-height:20px;width:880px;margin:6px auto 0}
.btn{display:inline-block;background:var(--green);color:#fff;font-size:11px;text-transform:uppercase}
.welcome .btn{width:126px;height:39px;line-height:39px;margin-top:24px}
.rule{left:88px;top:866px;width:1024px;height:1px;background:var(--line)}

/* portfolio */
.section-title{width:1200px;left:0;text-align:center;font-weight:300;font-size:30px}
.tabs{left:88px;top:955px;width:1024px;height:45px;border-bottom:2px solid var(--teal);display:flex;font-size:11px;color:#555}
.tabs .tab{padding:0 16px;line-height:43px;border-right:1px solid var(--line)}
.tabs .tab.on{background:var(--teal);color:#fff;position:relative;padding:0 18px}
.tabs .tab.on::after{content:"";position:absolute;left:50%;bottom:-9px;margin-left:-8px;border:8px solid transparent;border-top-color:var(--teal);border-bottom:0}
.tabs .search{margin-left:auto;display:flex;align-items:center;gap:14px;padding-right:18px;color:#777;font-size:11px}
.tabs .search .field{border-left:1px solid var(--line);padding-left:14px;width:235px}
.tabs .more{border-left:1px solid var(--line);padding-left:22px;display:flex;align-items:center;gap:8px;color:#444}
.tile{top:1025px;width:198px;height:267px}
.tile-over{background:rgba(27,132,201,.9);color:#fff;text-align:center;font-size:11px}
.tile-over h4{font-weight:400;margin-top:90px;font-size:11px}
.tile-over p{width:160px;margin:8px auto 0;line-height:16px}
.tile-over .acts{display:flex;justify-content:center;gap:6px;margin-top:12px}
.tile-over .acts span{width:30px;height:30px;background:#fff}
.tile-over .acts span.g{background:var(--green)}

/* jobs */
.jobs{left:0;top:1345px;width:1200px;height:505px;background:var(--panel);border:1px solid #ddd}
.jobs-tabs{left:425px;top:1440px;display:flex;gap:36px;font-size:11px;color:#444}
.jobs-tabs .on{color:var(--green);border-bottom:2px solid var(--green);padding-bottom:11px}
.jobs-line{left:88px;top:1470px;width:1024px;height:1px;background:var(--line)}
.search-circle{left:1067px;top:1405px;width:42px;height:42px;border-radius:50%;background:#e4e4e4}
.th{top:1514px;font-size:11px;color:#666;text-transform:uppercase}
.row-line{left:88px;width:1024px;height:1px;background:#ddd}
.cell{font-size:12px;color:#333}
.logo-dot{width:30px;height:30px;border-radius:50%}
.badge{width:122px;height:30px;color:#fff;font-size:11px;text-align:center;line-height:30px;font-weight:500}
.apply{width:97px;height:34px;background:var(--teal);color:#fff;font-size:11px;text-align:center;line-height:34px}

/* blog */
.story-img{top:1950px;height:287px}
.story{top:2120px;height:168px;padding:22px 24px;font-size:11.5px;line-height:19px}
.story h5{font-size:16px;font-weight:400;margin-bottom:10px}
.story.white{background:#fff;border:1px solid #ccc;color:#777}
.story.white h5{color:#444}
.story.green{background:var(--green);color:#fff}
.story .more{display:block;margin-top:6px}

/* footer */
.footer{left:0;top:2352px;width:1200px;height:258px;background:#f4f4f4;border-top:1px solid #ddd}
.f-col{top:2385px;font-size:11px;color:#444;line-height:18px}
.f-col h6{font-size:14px;font-weight:400;color:#333;margin-bottom:14px}
.f-links{display:grid;grid-template-columns:115px 100px;row-gap:11px}
.social{display:flex;gap:8px;margin-top:12px}
.social i{width:34px;height:34px;border-radius:50%;background:var(--blue)}
.tweet{display:flex;gap:8px;padding-bottom:10px;border-bottom:1px solid #ddd;margin-bottom:10px}
.tweet b{width:10px;height:10px;border-radius:50%;background:var(--sky);flex:none;margin-top:4px}
.email{width:254px;height:40px;border:1px solid #ccc;background:#fff;padding-left:18px;line-height:38px;color:#888}
.subscribe{margin-top:10px;width:118px;height:36px;background:var(--blue-bright);color:#fff;text-align:center;line-height:36px;font-size:11px;font-weight:500}
.copyright{left:0;top:2610px;width:1200px;height:45px;background:var(--teal);color:#fff;text-align:center;line-height:45px;font-size:11px}
</style>
</head>
<body>

<header class="abs topbar">
  <div class="abs brand"><span class="brand-dot"></span>PathVerdantia</div>
  <nav class="abs nav">
    <a class="active">Home</a><a>About Us</a><a>Portfolio</a><a>Blog</a><a>Contact Us</a>
  </nav>
  <div class="abs account">
    <span><svg width="10" height="11" viewBox="0 0 10 11"><rect x="1" y="5" width="8" height="6" fill="#fff"/><path d="M3 5V3a2 2 0 0 1 4 0v2" stroke="#fff" fill="none" stroke-width="1.4"/></svg>Sign Up</span>
    <span><svg width="10" height="11" viewBox="0 0 10 11"><circle cx="5" cy="3" r="2.6" fill="#fff"/><path d="M0 11a5 4.5 0 0 1 10 0z" fill="#fff"/></svg>Login</span>
  </div>
</header>

<section class="abs hero" role="img" aria-label="Photo of smiling professionals collaborating in a bright office"></section>
<div class="abs hero-arrow" style="left:0"><svg width="34" height="34"><path d="M19 12l-5 5 5 5" stroke="#fff" fill="none" stroke-width="2"/></svg></div>
<div class="abs hero-arrow right" style="left:1166px"><svg width="34" height="34"><path d="M15 12l5 5-5 5" stroke="#fff" fill="none" stroke-width="2"/></svg></div>
<div class="abs hero-card">
  <div class="site">PathVerdantia.com</div>
  <h2>Searching Job</h2>
  <p>In One Click</p>
  <div class="dots"><i></i><i class="on"></i><i></i></div>
</div>

<section class="abs welcome">
  <h3>Welcome To</h3>
  <h1>PathVerdantia</h1>
  <p>Lorem ipsum dolor sit amet, consectetuer adipiscing elit. Aenean commodo ligula eget dolor aenean massa. Cum sociis natoque penatibus et magnis dis parturient montes, nascetur ridiculus mus donec quam felis ultricies nec pellentesque .</p>
  <span class="btn">Read More</span>
</section>
<div class="abs rule"></div>

<h2 class="abs section-title" style="top:900px">Our Portfolio</h2>
<div class="abs tabs">
  <span class="tab on">All</span><span class="tab">Public Health</span><span class="tab">Technology</span><span class="tab">Sustainable Cities</span>
  <div class="search">
    <svg width="11" height="11" viewBox="0 0 11 11"><circle cx="4.5" cy="4.5" r="3.6" stroke="#666" fill="none" stroke-width="1.3"/><path d="M7 7l3.4 3.4" stroke="#666" stroke-width="1.3"/></svg>
    <span class="field">Search by talent types and focus areas...</span>
    <span class="more">MORE <svg width="10" height="6"><path d="M1 1l4 4 4-4" stroke="var(--teal)" fill="none" stroke-width="1.5"/></svg></span>
  </div>
</div>
<div class="abs tile" style="left:86px;background:linear-gradient(135deg,#eee5dc,#c9b8a6)" role="img" aria-label="Photo of a hand filling in a form"></div>
<div class="abs tile" style="left:290px;background:linear-gradient(135deg,#6fa6c9,#2d6f9f)" role="img" aria-label="Photo of a team meeting behind a project overlay"></div>
<div class="abs tile tile-over" style="left:290px">
  <h4>PROJECT</h4>
  <p>Lorem ipsum dolor sit amet consectetuer adipiscing elit commodo .</p>
  <div class="acts"><span></span><span class="g"></span></div>
</div>
<div class="abs tile" style="left:496px;background:linear-gradient(135deg,#6b6560,#2e2b2a)" role="img" aria-label="Photo of colleagues seated at a conference table"></div>
<div class="abs tile" style="left:705px;background:linear-gradient(135deg,#3a3f46,#c8ccd0)" role="img" aria-label="Photo of a resume handed across a desk"></div>
<div class="abs tile" style="left:911px;background:linear-gradient(135deg,#d8dde2,#6e7a88)" role="img" aria-label="Photo of two businessmen reviewing a tablet"></div>

<section class="abs jobs"></section>
<h2 class="abs section-title" style="top:1382px">Find A Good Job</h2>
<div class="abs search-circle"><svg width="42" height="42"><circle cx="19.5" cy="19.5" r="5" stroke="#777" fill="none" stroke-width="1.5"/><path d="M23 23l4 4" stroke="#777" stroke-width="1.5"/></svg></div>
<div class="abs jobs-tabs"><span class="on">For Job Seeker</span><span>For Companies</span><span>Find Candidates</span></div>
<div class="abs jobs-line"></div>
<span class="abs th" style="left:88px">Job Title</span>
<span class="abs th" style="left:477px">By</span>
<span class="abs th" style="left:622px">Option</span>
<span class="abs th" style="left:752px">Location</span>
<span class="abs th" style="left:885px">Budget</span>

<div class="abs logo-dot" style="left:92px;top:1553px;background:var(--blue)"></div>
<span class="abs cell" style="left:175px;top:1563px">Professional Front-end Developer</span>
<span class="abs cell" style="left:477px;top:1563px">Larkwell</span>
<div class="abs badge" style="left:588px;top:1556px;background:var(--sky)">Full Time</div>
<span class="abs cell" style="left:752px;top:1563px">New York City</span>
<span class="abs cell" style="left:888px;top:1563px">24$ /h</span>
<div class="abs apply" style="left:1018px;top:1551px">Apply</div>
<div class="abs row-line" style="top:1615px"></div>

<div class="abs logo-dot" style="left:92px;top:1645px;background:#333"></div>
<span class="abs cell" style="left:175px;top:1655px">Webdesigner Leader</span>
<span class="abs cell" style="left:477px;top:1655px">Quillory</span>
<div class="abs badge" style="left:588px;top:1648px;background:var(--orange)">InternShip</div>
<span class="abs cell" style="left:752px;top:1655px">New York City</span>
<span class="abs cell" style="left:888px;top:1655px">24$ /h</span>
<div class="abs apply" style="left:1018px;top:1643px">Apply</div>
<div class="abs row-line" style="top:1707px"></div>

<div class="abs logo-dot" style="left:92px;top:1738px;background:var(--teal)"></div>
<span class="abs cell" style="left:175px;top:1748px">Personal Trainer</span>
<span class="abs cell" style="left:477px;top:1748px">Venmara</span>
<div class="abs badge" style="left:588px;top:1741px;background:var(--green)">Project</div>
<span class="abs cell" style="left:752px;top:1748px">New York City</span>
<span class="abs cell" style="left:888px;top:1748px">24$ /h</span>
<div class="abs apply" style="left:1018px;top:1736px">Apply</div>
<div class="abs row-line" style="top:1800px"></div>

<h2 class="abs section-title" style="top:1885px">Steering Through Seams</h2>
<div class="abs story-img" style="left:91px;width:497px;background:linear-gradient(135deg,#d6dbe0,#8a9aa8 60%,#c2ccd4)" role="img" aria-label="Photo of a smiling young man in an office"></div>
<div class="abs story-img" style="left:616px;width:496px;background:linear-gradient(135deg,#9ec3e0,#d9e8f3 55%,#6a9cc4)" role="img" aria-label="Photo of hands typing on a laptop"></div>
<article class="abs story white" style="left:108px;width:460px">
  <h5>Donec pede justo, fringilla vel .</h5>
  Lorem ipsum dolor sit amet, consectetuer adipiscing elit. Aenean com-modo ligula eget dolor. Aenean massa. Cum sociis natoque penatibus et magnis dis parturient montes.
  <span class="more">Read More</span>
</article>
<article class="abs story green" style="left:632px;width:462px">
  <h5>Donec pede justo, fringilla vel .</h5>
  Lorem ipsum dolor sit amet, consectetuer adipiscing elit. Aenean com-modo ligula eget dolor. Aenean massa. Cum sociis natoque penatibus et magnis dis parturient montes.
  <span class="more">Read More</span>
</article>

<footer class="abs footer"></footer>
<div class="abs f-col" style="left:88px;width:240px">
  <div style="display:flex;align-items:center;gap:9px;font-size:16px;margin-bottom:12px"><span style="width:28px;height:28px;border-radius:50%;background:var(--teal)"></span>PathVerdantia</div>
  Lorem ipsum dolor sit amet, consectetuer adipiscing elit. Aenean commodo ligula eget dolor. Aenean massa. Cum sociis natoque penatibus et magnis dis .
  <div class="social" aria-label="Social links"><i></i><i style="background:var(--sky)"></i><i style="background:var(--teal)"></i><i style="background:var(--blue-bright)"></i></div>
</div>
<div class="abs f-col" style="left:353px">
  <h6>Site Map</h6>
  <div class="f-links"><span>Home</span><span>Features</span><span>Search a Job</span><span>Privacy Policy</span><span>Post a Job</span><span>Terms of Use</span><span>How It Works</span><span>Contact Us</span></div>
</div>
<div class="abs f-col" style="left:600px;width:240px">
  <h6>Chirpline Widget</h6>
  <div class="tweet"><b></b><span>Be yourself; everyone else is already - Marlowe #PathVerdantia lnk.ex/4QR2TZ</span></div>
  <div class="tweet" style="border:0"><b></b><span>Be yourself; everyone else is already - Marlowe #PathVerdantia lnk.ex/4QR2TZ</span></div>
</div>
<div class="abs f-col" style="left:857px">
  <h6>Sign Up for our newsletter</h6>
  <div class="email">Email Address</div>
  <div class="subscribe">SUBSCRIBE</div>
</div>
<div class="abs copyright">Copyright2016 | All Right Reserved</div>

</body>
</html>
```